Wir sind eine mobile Cocktailbar ! Wir arbeiten vielen Veranstaltungen / Festivals.
Ein sehr wichtiges Geschäftssegment sind Firmenveranstaltungen jeglicher Größe.
Hier stehen wir für sehr hohe Qualität an Service und an den Drinks.
Wir arbeiten stets mit Markenprodukten, professionellen Barkeepern und sehr hochwertigen Equipment
Unsere Website ist www.glaswinkel-bar.de
Es soll schlicht aber hochwertig sein
vielleicht eine Layout im Hintergrund
Drinks, Flüssigkeit, Bartending etc
Gerne auch das Logo eingebaut

```html
<!DOCTYPE html>
<html lang="de">
<head>
<meta charset="utf-8">
<title>Glaswinkel – Mobile Cocktailbar</title>
<link href="https://fonts.googleapis.com/css2?family=Montserrat:ital,wght@0,300;0,400;0,700;1,700&display=swap" rel="stylesheet">
<style>
  :root {
    --ink: #000000;
    --paper: #ffffff;
    --text: #1a1a1a;
    --faint: #efefef;
    --photo-dark: #0a0a0c;
    --photo-red: #8a1f24;
  }
  * { margin: 0; padding: 0; box-sizing: border-box; }
  html, body { width: 849px; height: 1200px; overflow: hidden; background: var(--paper); }
  body { font-family: "Montserrat", sans-serif; color: var(--text); }

  .letterhead { position: relative; width: 849px; height: 1200px; background: var(--paper); }

  .header-band {
    position: absolute; left: 0; top: 0; width: 849px; height: 257px; background: var(--ink);
  }
  .hero-photo {
    position: absolute; left: 0; top: 0; width: 380px; height: 468px;
    background:
      radial-gradient(ellipse 90px 150px at 155px 250px, var(--photo-red) 0%, rgba(138,31,36,0.4) 55%, transparent 100%),
      radial-gradient(ellipse 260px 60px at 230px 360px, #26272b 0%, transparent 100%),
      var(--photo-dark);
  }

  .brand-plate {
    position: absolute; left: 416px; top: 84px; width: 353px; height: 42px;
    background: var(--paper);
    display: flex; align-items: center; justify-content: center;
  }
  .brand-name {
    font-weight: 700; font-size: 25px; letter-spacing: 6px; color: var(--ink);
    padding-left: 6px;
  }
  .brand-url {
    position: absolute; left: 416px; top: 132px; width: 353px; text-align: center;
    font-weight: 700; font-size: 8.5px; letter-spacing: 2.6px; color: var(--paper);
  }

  .contact-list {
    position: absolute; left: 406px; top: 281px; list-style: none;
  }
  .contact-item {
    display: flex; align-items: center; height: 30.8px;
    font-size: 9.8px; font-weight: 400; color: var(--text);
  }
  .contact-icon { width: 19px; height: 19px; margin-right: 25px; flex: none; }

  .section-title {
    position: absolute; left: 0; top: 533px; width: 880px; text-align: center;
    font-weight: 700; font-style: italic; font-size: 20px; letter-spacing: 3.4px; color: var(--ink);
  }

  .intro-text {
    position: absolute; left: 28px; top: 624px; width: 788px; text-align: center;
    font-weight: 300; font-size: 16.6px; line-height: 20.6px; letter-spacing: 0.12px; color: var(--text);
  }

  .bar-illustration {
    position: absolute; left: 307px; top: 935px; width: 237px; height: 178px;
    background: radial-gradient(ellipse 50% 50% at 50% 55%, #f1f1f1 0%, #f6f6f6 55%, rgba(255,255,255,0) 100%);
  }

  .footer-rule {
    position: absolute; left: 62px; top: 1124px; width: 726px; height: 4px; background: var(--ink);
  }
</style>
</head>
<body>
<main class="letterhead">
  <div class="header-band"></div>
  <div class="hero-photo" role="img" aria-label="Foto: roter Longdrink im Kristallglas mit Strohhalm und Minze auf Schieferplatte, daneben Limettenscheibe und Garnituren, dunkler Hintergrund"></div>

  <div class="brand-plate"><span class="brand-name">GLASWINKEL</span></div>
  <div class="brand-url">www.glaswinkel-bar.de</div>

  <ul class="contact-list">
    <li class="contact-item">
      <svg class="contact-icon" viewBox="0 0 20 20"><circle cx="10" cy="10" r="10" fill="#000"/><rect x="6.5" y="5" width="7" height="10" rx="1.2" fill="none" stroke="#fff" stroke-width="1.4"/><circle cx="10" cy="11.5" r="1.2" fill="#fff"/></svg>
      Mobile Cocktailbar
    </li>
    <li class="contact-item">
      <svg class="contact-icon" viewBox="0 0 20 20"><circle cx="10" cy="10" r="10" fill="#000"/><rect x="6" y="5" width="8" height="10" rx="1.2" fill="none" stroke="#fff" stroke-width="1.4"/><path d="M8.2 8.2c.4 1.7 1.5 2.9 3.3 3.5l.8-.9" fill="none" stroke="#fff" stroke-width="1.2"/></svg>
      Phone
    </li>
    <li class="contact-item">
      <svg class="contact-icon" viewBox="0 0 20 20"><circle cx="10" cy="10" r="10" fill="#000"/><path d="M10 15s-3.5-3.6-3.5-6.3a3.5 3.5 0 0 1 7 0C13.5 11.4 10 15 10 15z" fill="none" stroke="#fff" stroke-width="1.4"/><circle cx="10" cy="8.7" r="1.2" fill="#fff"/></svg>
      Location
    </li>
    <li class="contact-item">
      <svg class="contact-icon" viewBox="0 0 20 20"><circle cx="10" cy="10" r="10" fill="#000"/><path d="M7 6l5 5M10.5 5.5l4 4-2.5.5-2 2-.5 2.5-4-4 2.5-.5 2-2z" fill="#fff"/><path d="M8 12l-2.5 2.5" stroke="#fff" stroke-width="1.3"/></svg>
      Address
    </li>
    <li class="contact-item">
      <svg class="contact-icon" viewBox="0 0 20 20"><circle cx="10" cy="10" r="10" fill="#000"/><circle cx="10" cy="10" r="5" fill="none" stroke="#fff" stroke-width="1.4"/><path d="M5 10h10M10 5c-2 2.8-2 7.2 0 10M10 5c2 2.8 2 7.2 0 10" fill="none" stroke="#fff" stroke-width="1"/></svg>
      Website
    </li>
    <li class="contact-item">
      <svg class="contact-icon" viewBox="0 0 20 20"><circle cx="10" cy="10" r="10" fill="#000"/><rect x="5" y="6.5" width="10" height="7" rx="1" fill="#fff"/><path d="M5.3 7l4.7 3.5L14.7 7" fill="none" stroke="#000" stroke-width="1.1"/></svg>
      Mail
    </li>
  </ul>

  <h1 class="section-title">MOBILE COCKTAILBAR</h1>

  <p class="intro-text">Lorem ipsum dolor sit amet, consectetur adipiscing elit. Proin pretium neque at nibh ultricies, vel pretium risus volutpat. Fusce rhoncus, elit eu facilisis ultricies, velit leo pharetra sem, quis dignissim sapien lorem nec dui. Praesent dignissim tortor ante, quis venenatis ex tempus sed. Nulla turpis mauris, mollis non felis eu, egestas lobortis lectus. Nulla aliquet felis eget ullamcor&shy;per gravida. Nullam risus ipsum, sagittis vitae maximus quis, accumsan vel dolor. Curabitur metus quam, semper id semper at, bibendum eget diam. Curabitur vitae luctus neque. Ves&shy;tibulum rhoncus ac nisl vitae porttitor. Morbi fringilla varius mi at imperdiet. Vestibulum aliquet, justo sed commodo ultrices, nulla libero elementum urna, sit amet porta felis dolor eu purus.</p>

  <div class="bar-illustration" role="img" aria-label="Dezente helle Strichillustration: Martiniglas mit Olive, Cocktailshaker und Schale"></div>

  <div class="footer-rule"></div>
</main>
</body>
</html>
```